Professional Business Card - TWO SIDES

I need a new business card design to be used by myself and my employees. I would like a professional card and for the front I thought I would like a dark blue thatch with our logo in a raised gold foil on top of it. On the other side I would like name, position, and contact info. I've uploaded our old design for an example of the info used.

Target Market(s)

Business Clients

Industry/Entity Type

CPA Firm

Contact Information for Business Card

Logo, Name, Title, Address, Phone Numbers, Website address, Email Address

Font styles to use
Serif
Sans Serif

Colors
0054AA
0677BA
7BADD7
CADEEF
E8F1F8
0094D4
00A9DD
6FCCEA
C7EBF8
E9F6FB

Requirements
Must have
• Modern Professional Look
Nice to have
• Logo in Gold Foil or ability to have is raised. I like our logo in a single color
Should not have
• I've uploaded old business card

```html
<!DOCTYPE html>
<html lang="en">
<head>
<meta charset="utf-8">
<title>Hale &amp; Hale – Business Card</title>
<link rel="stylesheet" href="https://fonts.googleapis.com/css2?family=Montserrat:wght@400;500;600;700&display=swap">
<style>
  :root {
    --page: #e6e8eb;
    --navy: #16365f;
    --navy-ink: #13325a;
    --gold: #c99b3c;
    --white: #ffffff;
    --ink: #1d1f24;
    --ghost: #f1f2f3;
  }
  * { box-sizing: border-box; margin: 0; padding: 0; }
  html, body {
    width: 1200px; height: 900px; overflow: hidden;
    background: var(--page);
    font-family: "Montserrat", sans-serif;
  }
  .sheet {
    position: relative; width: 1200px; height: 900px;
    display: flex; flex-direction: column; align-items: center; justify-content: center; gap: 36px;
  }
  .card {
    position: relative; width: 620px; height: 354px; overflow: hidden;
    box-shadow: 0 10px 28px rgba(0,0,0,.18);
  }
  /* Front */
  .card--front { background: var(--navy); display: flex; align-items: center; justify-content: center; }
  .brand-name {
    font-family: "Montserrat", sans-serif; font-weight: 700;
    letter-spacing: .02em; text-transform: uppercase; white-space: nowrap;
  }
  .card--front .brand-name { color: var(--gold); font-size: 58px; }
  /* Back */
  .card--back { background: var(--white); }
  .card--back .brand-name {
    position: absolute; left: 38px; top: 40px;
    color: var(--navy-ink); font-size: 38px;
  }
  .ghost-square {
    position: absolute; right: -40px; top: 120px;
    width: 260px; height: 260px; border-radius: 28px;
    background: var(--ghost);
  }
  .contact {
    position: absolute; left: 38px; bottom: 36px;
    color: var(--ink); font-size: 14px; line-height: 1.5; font-weight: 400;
  }
  .contact__address { margin-bottom: 4px; }
  .contact__row { display: flex; align-items: center; gap: 8px; }
  .contact__row svg { width: 12px; height: 12px; flex: none; fill: var(--navy-ink); }
  .person {
    position: absolute; right: 44px; top: 196px; text-align: right;
  }
  .person__name {
    color: var(--navy-ink); font-weight: 700; font-size: 22px; letter-spacing: .03em;
  }
  .person__title { color: var(--ink); font-size: 14px; font-weight: 500; letter-spacing: .03em; }
  .accent-bar {
    position: absolute; right: 16px; top: 200px;
    width: 12px; height: 50px; background: var(--navy-ink);
  }
</style>
</head>
<body>
<main class="sheet">
  <section class="card card--front" aria-label="Card front">
    <p class="brand-name">Hale &amp; Hale</p>
  </section>

  <section class="card card--back" aria-label="Card back">
    <div class="ghost-square" aria-hidden="true"></div>
    <p class="brand-name">Hale &amp; Hale</p>

    <div class="contact">
      <p class="contact__address">2140 N. Alder Street<br>Region Name, AB 40218</p>
      <p class="contact__row">
        <svg viewBox="0 0 24 24" aria-hidden="true"><path d="M6.6 10.8a15.1 15.1 0 0 0 6.6 6.6l2.2-2.2c.3-.3.7-.4 1-.2 1.1.4 2.3.6 3.6.6.6 0 1 .4 1 1V20c0 .6-.4 1-1 1C10.6 21 3 13.4 3 4c0-.6.4-1 1-1h3.5c.6 0 1 .4 1 1 0 1.3.2 2.5.6 3.6.1.3 0 .7-.2 1z"/></svg>
        (877) 555 0142
      </p>
      <p class="contact__row">
        <svg viewBox="0 0 24 24" aria-hidden="true"><path d="M2 5h20v14H2zm2 2v.5l8 5 8-5V7l-8 5z"/></svg>
        info@halehale.com
      </p>
      <p class="contact__row">
        <svg viewBox="0 0 24 24" aria-hidden="true"><path d="M12 2a10 10 0 1 0 0 20 10 10 0 0 0 0-20zm6.9 6h-3a15 15 0 0 0-1.3-3.8A8 8 0 0 1 18.9 8zM12 4c.8 1.2 1.5 2.5 1.9 4h-3.8c.4-1.5 1.1-2.8 1.9-4zM4.3 14a8 8 0 0 1 0-4h3.4a16 16 0 0 0 0 4zm.8 2h3a15 15 0 0 0 1.3 3.8A8 8 0 0 1 5.1 16zm3-8h-3a8 8 0 0 1 4.3-3.8C8.8 5.4 8.4 6.7 8.1 8zM12 20c-.8-1.2-1.5-2.5-1.9-4h3.8c-.4 1.5-1.1 2.8-1.9 4zm2.3-6H9.7a14.7 14.7 0 0 1 0-4h4.6a14.7 14.7 0 0 1 0 4zm.3 5.8c.6-1.2 1-2.5 1.3-3.8h3a8 8 0 0 1-4.3 3.8zM16.3 14a16 16 0 0 0 0-4h3.4a8 8 0 0 1 0 4z"/></svg>
        www.halehale.com
      </p>
    </div>

    <div class="person">
      <p class="person__name">DANIEL REYES</p>
      <p class="person__title">Founder</p>
    </div>
    <div class="accent-bar" aria-hidden="true"></div>
  </section>
</main>
</body>
</html>
```